Construction business card

We are a family run and family oriented business in Philadelphia and we are starting new. We proudly serve the public by giving our customers great work at affordable prices. We can do all aspects of construction from the roof to the basement. We would like our business card to incorporate tools and family.
Updates

Can y'all please incorporate a bulldog

Industry/Entity Type

Construction

Contact Information for Business Card

Harwick Builders LLC, Dennis Oakley, 7819 W Lindel st Philadelphia Pa 19188, CEO Main phone (215) 555-0193 cellphone 215-555-0147 Dennis oakley Jr cellphone 267-555-0162 email harwickbuildersllc@mailtrove.example

Colors
f78f20
ffffff
1b1b1b

```html
<!DOCTYPE html>
<html lang="en">
<head>
<meta charset="UTF-8">
<title>Harwick Builders LLC — Business Card</title>
<link rel="stylesheet" href="https://fonts.googleapis.com/css2?family=PT+Sans:wght@400;700&display=swap">
<style>
  :root {
    --backdrop: #d8d3cf;
    --card-white: #ffffff;
    --card-blue: #3d6e9c;
    --ink: #1b1b1b;
    --logo-grey: #4a4a4a;
    --accent: #f78f20;
  }
  * { margin: 0; padding: 0; box-sizing: border-box; }
  html, body {
    width: 1200px;
    height: 800px;
    overflow: hidden;
    background: var(--backdrop);
    font-family: "PT Sans", sans-serif;
  }
  .business-card {
    position: absolute;
    left: 180px;
    top: 160px;
    width: 840px;
    height: 480px;
    background: var(--card-white);
    overflow: hidden;
    box-shadow: 0 10px 30px rgba(0, 0, 0, 0.18);
  }
  .card-band {
    position: absolute;
    inset: 0;
    width: 100%;
    height: 100%;
  }
  .card-band .band-shape { fill: var(--card-blue); }
  .brand-lockup {
    position: absolute;
    left: 60px;
    top: 56px;
    display: flex;
    align-items: center;
    gap: 20px;
  }
  .brand-mark {
    width: 56px;
    height: 56px;
    background: var(--accent);
    flex: none;
  }
  .brand-name {
    font-size: 64px;
    font-weight: 700;
    color: var(--logo-grey);
    white-space: nowrap;
  }
  .contact-block {
    position: absolute;
    left: 60px;
    top: 250px;
    color: var(--ink);
  }
  .person-name {
    font-size: 46px;
    font-weight: 700;
    line-height: 1.1;
    white-space: nowrap;
  }
  .person-title {
    font-weight: 400;
    font-size: 34px;
  }
  .street-address {
    margin-top: 26px;
    font-size: 34px;
    font-weight: 400;
    white-space: nowrap;
  }
</style>
</head>
<body>
  <article class="business-card">
    <svg class="card-band" viewBox="0 0 840 480" preserveAspectRatio="none" aria-hidden="true">
      <path class="band-shape" d="M0,200 Q430,190 840,330 L840,480 L0,480 Z"/>
    </svg>

    <div class="brand-lockup">
      <span class="brand-mark" aria-hidden="true"></span>
      <span class="brand-name">Harwick Builders LLC</span>
    </div>

    <div class="contact-block">
      <p class="person-name">Dennis Oakley, <span class="person-title">CEO</span></p>
      <p class="street-address">7819 W Lindel st Philadelphia Pa 19188</p>
    </div>
  </article>
</body>
</html>
```